professional business card

Professional business card with logo on one side, and underneath logo list:
- power
-data
-fibre optic
-isolar

On other side:
Marcus Webb
Owner
MOB 0432 958 720
marcus@vorn.com.au
www.vornelectrical.com.au

Please edit logo to just leave VORN

```html
<!DOCTYPE html>
<html lang="en">
<head>
<meta charset="utf-8">
<title>Vorn Electrical – Business Card</title>
<link rel="stylesheet" href="https://fonts.googleapis.com/css2?family=Montserrat:wght@600&family=Lato:wght@300;400&display=swap">
<style>
  :root {
    --page-bg: #e4e5e6;
    --card-top: #ffffff;
    --card-bottom: #dedfe0;
    --teal: #13999a;
    --band-dark: #4b4d4e;
    --text-light: #e9eaea;
    --name-grey: #d6d7d8;
  }
  * { margin: 0; padding: 0; box-sizing: border-box; }
  html, body {
    width: 1200px;
    height: 1176px;
    overflow: hidden;
    background: var(--page-bg);
  }
  .business-card {
    position: absolute;
    left: 200px;
    top: 338px;
    width: 782px;
    height: 447px;
    border-radius: 22px;
    overflow: hidden;
    background: linear-gradient(170deg, var(--card-top) 35%, var(--card-bottom) 100%);
    box-shadow: 0 10px 24px rgba(0, 0, 0, 0.18);
  }
  .brand-name {
    position: absolute;
    left: 0;
    right: 0;
    top: 36px;
    text-align: center;
    font-family: "Montserrat", sans-serif;
    font-weight: 600;
    font-size: 112px;
    line-height: 1;
    letter-spacing: 2px;
    color: var(--teal);
  }
  .accent-rule {
    position: absolute;
    left: 0;
    top: 186px;
    width: 100%;
    height: 4px;
    background: var(--teal);
  }
  .contact-band {
    position: absolute;
    left: 0;
    top: 194px;
    width: 100%;
    height: 170px;
    background: var(--band-dark);
  }
  .person {
    position: absolute;
    right: 424px;
    top: 50px;
    text-align: right;
    font-family: "Lato", sans-serif;
  }
  .person-name {
    font-weight: 400;
    font-size: 35px;
    line-height: 1;
    color: var(--name-grey);
    text-transform: uppercase;
    letter-spacing: -0.3px;
  }
  .person-role {
    margin-top: 6px;
    font-weight: 400;
    font-size: 18px;
    line-height: 1;
    color: var(--teal);
    text-transform: uppercase;
  }
  .divider {
    position: absolute;
    left: 389px;
    top: 30px;
    width: 2px;
    height: 110px;
    background: var(--teal);
  }
  .contact-list {
    position: absolute;
    left: 422px;
    top: 36px;
    list-style: none;
    font-family: "Lato", sans-serif;
    font-size: 20px;
    color: var(--text-light);
  }
  .contact-item {
    display: flex;
    align-items: center;
    height: 36px;
  }
  .contact-icon {
    width: 14px;
    height: 16px;
    margin-right: 10px;
    flex-shrink: 0;
  }
  .services-band {
    position: absolute;
    left: 0;
    top: 372px;
    width: 100%;
    height: 28px;
    background: var(--teal);
  }
  .services-list {
    display: flex;
    justify-content: center;
    align-items: center;
    height: 100%;
    padding-right: 10px;
    list-style: none;
    font-family: "Lato", sans-serif;
    font-size: 20px;
    color: #ffffff;
    text-transform: uppercase;
  }
  .service + .service::before {
    content: "I";
    margin: 0 20px;
  }
</style>
</head>
<body>
  <main class="business-card">
    <div class="brand-name">VORN</div>
    <div class="accent-rule"></div>

    <section class="contact-band">
      <div class="person">
        <p class="person-name">Marcus Webb</p>
        <p class="person-role">Owner</p>
      </div>
      <div class="divider"></div>
      <ul class="contact-list">
        <li class="contact-item">
          <svg class="contact-icon" viewBox="0 0 14 16" aria-hidden="true">
            <rect x="3" y="0.5" width="8" height="15" rx="1.5" fill="none" stroke="#13999a" stroke-width="1.6"/>
            <circle cx="7" cy="13" r="0.9" fill="#13999a"/>
          </svg>
          <span>0432 958 720</span>
        </li>
        <li class="contact-item">
          <svg class="contact-icon" viewBox="0 0 14 16" aria-hidden="true">
            <rect x="0" y="4" width="14" height="9" fill="#13999a"/>
            <polyline points="0,4 7,9.5 14,4" fill="none" stroke="#4b4d4e" stroke-width="1.2"/>
          </svg>
          <span>marcus@vorn.com.au</span>
        </li>
        <li class="contact-item">
          <svg class="contact-icon" viewBox="0 0 14 16" aria-hidden="true">
            <g fill="none" stroke="#13999a" stroke-width="1">
              <circle cx="7" cy="9" r="6"/>
              <ellipse cx="7" cy="9" rx="2.6" ry="6"/>
              <line x1="1" y1="9" x2="13" y2="9"/>
            </g>
          </svg>
          <span>www.vornelectrical.com.au</span>
        </li>
      </ul>
    </section>

    <section class="services-band">
      <ul class="services-list">
        <li class="service">Power</li>
        <li class="service">Data</li>
        <li class="service">Fibre Optic</li>
        <li class="service">Solar</li>
      </ul>
    </section>
  </main>
</body>
</html>
```